Bright Harbor Goods - Product Page

Looking for a design for our product pages to showcase all of the following information in an aesthetically pleasing way. <br/><br/>• Product price per piece & price breaks<br/>• Set up cost <br/>• Additional color cost<br/>• Imprint side <br/>• Product Dimensions<br/><br/>Attached are photos showing ideas we have come up with to display the information. <br/><br/>The link below shows how our product pages is currently laid out. <br/><br/>Link to webpage: https://www.brightharborgoods.example/non-woven-reusable-promo-totes.html<br/>

Number of Pages Required

1 page

Colors
33b8a4
33a6d7
3277b5
fece3e
f9a040
a3cd3a

Requirements
Must have
• • Product price per piece & price breaks
• • Set up cost
• • Additional color cost
• • Imprint side
• • Product Dimensions

```html
<!DOCTYPE html>
<html lang="en">
<head>
<meta charset="utf-8">
<title>Non-Woven Reusable Promo Totes – Bright Harbor Goods</title>
<link href="https://fonts.googleapis.com/css2?family=Fira+Sans:wght@400;500;600&family=Open+Sans:wght@400;600;700&display=swap" rel="stylesheet">
<style>
:root{
  --teal:#33b8a4; --sky:#33a6d7; --blue:#3277b5; --navy:#16406e; --yellow:#f7e514;
  --orange:#f9a040; --orange-dk:#f08a2c; --green:#a3cd3a; --star:#fece3e;
  --gray-bg:#ebebeb; --card:#f1f1f1; --line:#dcdcdc; --text:#444; --dark:#222;
  --footer:#1b2a55; --footer-dk:#121c3c;
}
*{box-sizing:border-box;margin:0;padding:0}
html,body{width:1200px;height:2748px;overflow:hidden}
body{font-family:'Open Sans',sans-serif;color:var(--text);background:var(--gray-bg);position:relative;font-size:13px}
.abs{position:absolute}
h1,h2,h3,.fira{font-family:'Fira Sans',sans-serif;font-weight:500}
/* header */
.header{left:0;top:0;width:1200px;height:104px;background:#fff}
.brand{left:144px;top:36px;display:flex;align-items:center;gap:9px;font-family:'Fira Sans',sans-serif;font-size:23px;font-weight:600;color:#5aa632;white-space:nowrap}
.brand i{width:20px;height:20px;border-radius:50%;background:#5aa632;display:block}
.rush{left:430px;top:14px;width:74px;height:74px;border-radius:50%;background:#e8392b;border:4px solid #f3c3bd;color:#fff;text-align:center;font-weight:700;font-size:13px;line-height:15px;padding-top:14px}
.rush small{display:block;font-size:9px;color:#ffe34d}
.call{left:514px;top:28px;text-align:right;width:184px}
.call span{display:block;font-size:16px;color:#333}
.call b{display:block;font-size:24px;color:var(--blue);font-family:'Fira Sans',sans-serif;font-weight:500;white-space:nowrap}
.phoneic{left:704px;top:30px}
.search{left:752px;top:30px;width:240px;height:40px;border:1px solid #ccc;background:#f5f5f5;padding:11px 12px;color:#888;font-size:12px}
.search svg{position:absolute;right:10px;top:11px}
.cart{left:1016px;top:30px;width:40px;height:40px;border-radius:50%;background:var(--navy)}
.cart em{position:absolute;left:-6px;top:-2px;width:16px;height:16px;border-radius:50%;background:var(--orange);color:#fff;font-style:normal;font-size:9px;text-align:center;line-height:16px}
.nav{left:0;top:104px;width:1200px;height:41px;background:var(--navy)}
.nav ul{position:absolute;left:144px;display:flex;list-style:none;color:#fff;font-size:13.5px}
.nav li{padding:0 16px;line-height:41px}
.nav li.on{background:#0f2f54;padding:0 22px}
.crumb{left:0;top:145px;width:1200px;height:41px;background:#fff;border-bottom:1px solid #ddd;padding:12px 144px;font-size:11.5px;color:var(--navy)}
.crumb a{color:#e0392b;text-decoration:none;margin-right:10px}
.title{left:142px;top:204px;font-size:34px;color:var(--teal)}
/* product card */
.product{left:144px;top:267px;width:912px;height:983px;background:#fff}
.gallery{left:8px;top:8px;width:400px;height:530px;background:#f2f2f2}
.photo{position:absolute;background:linear-gradient(135deg,#d9302e 0%,#d9302e 45%,#c9a77a 55%,#c9a77a 100%)}
.thumb{position:absolute;width:70px;height:67px;background:#fff;border:1px solid #e3e3e3}
.thumb b{position:absolute;left:16px;top:12px;width:38px;height:46px;border-radius:2px}
.info{left:432px;top:12px;width:462px}
.sku{font-size:21px;color:var(--orange)}
.meta{font-size:11px;margin-top:8px;color:#555;white-space:nowrap}
.meta .st{color:var(--star);letter-spacing:1px}
.band{background:var(--green);color:#222;font-family:'Fira Sans',sans-serif;font-weight:600;font-size:16px;padding:6px 14px;margin-top:12px;height:30px}
table.price{width:462px;border-collapse:collapse;font-size:11.5px;background:#eee}
table.price td{border:1px solid #fff;height:25px;text-align:center;color:#333}
table.price td:first-child{width:50px}
.btns{display:flex;gap:8px;margin-top:10px}
.btns div{flex:1;height:40px;background:var(--teal);color:#fff;font-weight:700;font-size:12px;text-align:center;line-height:40px}
.optlabel{font-size:12.5px;font-weight:700;color:var(--navy);margin-top:18px}
.opts{display:flex;gap:11px;margin-top:6px}
.opt{flex:1;height:208px;background:#ededed}
.opt h3{font-size:16px;color:var(--blue);padding:8px 14px 0}
.opt p{font-size:10px;padding:0 14px 6px;color:#333}
.opt .inc{background:var(--yellow);font-size:10.5px;font-weight:700;color:#222;padding:8px 14px}
.opt dl{padding:8px 14px;font-size:8.5px;color:#333;display:grid;grid-template-columns:1fr 10px 70px;row-gap:5px}
.opt dd{text-align:right}
/* form */
.sample{left:8px;top:561px;width:896px;height:167px;background:var(--sky);padding:18px 16px}
.sample h2{color:#fff;text-align:center;font-size:26px;font-weight:400}
.fields{display:flex;gap:11px;margin-top:14px}
.fields div{flex:1;height:40px;background:#fff;padding:11px 14px;color:#777;font-size:13px;position:relative}
.submit{margin-top:8px;height:39px;background:var(--yellow);text-align:center;line-height:39px;font-size:14px;color:#333;font-weight:600}
.revhead{left:0;top:748px;width:912px;text-align:center;font-size:22px;color:var(--orange)}
.circ{display:inline-block;width:17px;height:17px;border-radius:50%;background:#666;vertical-align:middle;margin:0 16px 4px;position:relative}
.circ::after{content:"";position:absolute;top:5px;left:6px;border:4px solid transparent}
.circ.l::after{border-right:5px solid #fff;left:3px}
.circ.r::after{border-left:5px solid #fff;left:8px}
.rcard{top:787px;width:291px;height:188px;background:var(--card);padding:30px 30px;font-size:11.5px;line-height:19px;color:#555}
.rcard h4{font-size:12.5px;color:#222;font-weight:600;margin-bottom:12px}
.rcard h4 span{color:var(--star)}
/* tabs + details */
.tabs{left:144px;top:1267px;width:912px;height:47px;display:flex;background:#d4d4d4}
.tabs div{text-align:center;line-height:47px;font-size:15.5px;color:#666;border-right:1px solid #c4c4c4}
.tabs .on{background:var(--green);color:#222;position:relative}
.tabs .on::after{content:"";position:absolute;left:76px;bottom:-10px;border:10px solid transparent;border-top-color:var(--green);border-bottom:0}
.details{left:144px;top:1314px;width:912px;height:641px;background:#fff}
.details h2{font-size:22px;color:var(--orange);padding:24px 23px 14px;border-bottom:1px solid var(--line)}
.row{display:flex;height:44px;align-items:center;border-bottom:1px solid var(--line);font-size:13px;white-space:nowrap}
.row b{width:171px;padding-left:24px;font-weight:600;color:#222;white-space:nowrap}
.row i{font-style:normal;width:23px}
.feat{list-style:none;margin-left:193px;padding-top:4px;font-size:13px;line-height:32px}
.feat li::before{content:"• ";font-size:10px}
/* recommended */
.recs{left:144px;top:1972px;width:912px;height:320px;background:#fff}
.rec{position:absolute;top:64px;width:180px;text-align:center;font-size:11px;line-height:19px;color:#333}
.rec .pic{width:130px;height:125px;margin:0 auto 14px;border-radius:4px}
.rec .st{color:var(--star);font-size:13px;letter-spacing:1px}
.rec small{font-size:8.5px;display:block;line-height:12px}
/* footer */
.footer{left:0;top:2363px;width:1200px;height:385px;background:linear-gradient(180deg,#1f3163,#17244c)}
.footer h3{color:var(--orange);font-size:21px;font-weight:400;margin-bottom:18px}
.fcol{position:absolute;top:52px;color:#dfe4f0;font-size:11.5px;line-height:24px}
.fbrand{font-family:'Fira Sans',sans-serif;font-size:23px;font-weight:600;color:#fff;display:flex;gap:9px;align-items:center;white-space:nowrap;height:56px}
.fbrand i{width:18px;height:18px;border-radius:50%;background:#fff;display:block}
.social{display:flex;gap:22px;margin-top:18px}
.social b{width:16px;height:16px;border-radius:50%;background:#dfe4f0;display:block}
.copy{left:0;top:2680px;width:1200px;height:68px;background:var(--footer-dk);color:#dfe4f0;font-size:11.5px;text-align:center;line-height:68px}
.chat{left:1043px;top:2653px;width:157px;height:52px;border-radius:26px 0 0 26px;background:var(--green);color:#fff;font-weight:700;font-size:13px;padding:16px 0 0 68px}
.chat .face{position:absolute;left:0;top:-6px;width:62px;height:62px;border-radius:50%;border:3px solid #fff;background:linear-gradient(#c9a089,#6b3b2a)}
</style>
</head>
<body>
<header class="abs header">
  <div class="abs brand"><i></i>Bright Harbor Goods</div>
  <div class="abs rush">FREE<br>RUSH<small>Click Here</small></div>
  <div class="abs call"><span>Call Us Toll Free:</span><b>1-800-555-0142</b></div>
  <svg class="abs phoneic" width="24" height="40" viewBox="0 0 24 40"><rect x="2" y="1" width="20" height="38" rx="3" fill="none" stroke="#222" stroke-width="3"/><rect x="8" y="32" width="8" height="2" fill="#222"/></svg>
  <div class="abs search">Search<svg width="16" height="16" viewBox="0 0 16 16"><circle cx="6.5" cy="6.5" r="5" fill="none" stroke="#3a9a3a" stroke-width="2"/><path d="M10 10l5 5" stroke="#3a9a3a" stroke-width="2.4"/></svg></div>
  <div class="abs cart"><em>0</em><svg width="40" height="40" viewBox="0 0 40 40"><path d="M12 14h3l2 9h9l2-7H16" fill="none" stroke="#fff" stroke-width="2"/><circle cx="18" cy="26" r="1.6" fill="#fff"/><circle cx="25" cy="26" r="1.6" fill="#fff"/></svg></div>
</header>
<nav class="abs nav"><ul><li class="on">Home</li><li>Reusable Bags</li><li>Seed Paper</li><li>Reusable Bottles</li><li>Lanyards</li><li>Eco Promo Items</li><li>About Us</li><li>Blog</li><li>Contact Us</li></ul></nav>
<div class="abs crumb"><a>Home</a> »&nbsp;&nbsp; Non-Woven Reusable Promo Totes</div>
<h1 class="abs title">Non-Woven Reusable Promo Totes</h1>

<section class="abs product">
  <div class="abs gallery">
    <div class="photo" role="img" aria-label="Red and tan non-woven tote bags with printed logos" style="left:8px;top:8px;width:384px;height:290px;"></div>
    <div class="thumb" style="left:12px;top:310px"><b style="background:#222"></b></div>
    <div class="thumb" style="left:88px;top:310px"><b style="background:#1f4d2c"></b></div>
    <div class="thumb" style="left:164px;top:310px"><b style="background:#218a4e"></b></div>
    <div class="thumb" style="left:240px;top:310px"><b style="background:#8ccc4a"></b></div>
    <div class="thumb" style="left:316px;top:310px"><b style="background:#1b6fb5"></b></div>
    <div class="thumb" style="left:12px;top:383px"><b style="background:#23257a"></b></div>
    <div class="thumb" style="left:88px;top:383px"><b style="background:#d9302e"></b></div>
    <div class="thumb" style="left:164px;top:383px"><b style="background:#2a2a9c"></b></div>
    <div class="thumb" style="left:240px;top:383px"><b style="background:#b6a57f"></b></div>
    <div class="thumb" style="left:316px;top:383px"><b style="background:#1cb6b0"></b></div>
    <div class="thumb" style="left:12px;top:456px"><b style="background:#f2d640"></b></div>
    <div class="thumb" style="left:88px;top:456px"><b style="background:#5b2a9c"></b></div>
  </div>
  <div class="abs info">
    <div class="sku fira">SKU: PP2</div>
    <div class="meta">Size: 13" W x 14" H x 7" D &nbsp;|&nbsp; Thickness: 100 GSM &nbsp;<span class="st">★★★★★</span>&nbsp; 38 Review(s) &nbsp;|&nbsp; Add Review</div>
    <div class="band">IN-STOCK</div>
    <table class="price"><tr><td>Qty</td><td>1</td><td>100+</td><td>250+</td><td>500+</td><td>1,000+</td><td>2,500+</td><td>5,000+</td></tr>
    <tr><td>Price</td><td>$0.69</td><td>$1.46</td><td>$1.35</td><td>$1.30</td><td>$1.26</td><td>$1.23</td><td>$1.19</td></tr></table>
    <div class="band" style="margin-top:8px">OVERSEAS</div>
    <table class="price"><tr><td>Qty</td><td>1</td><td>1,000+</td><td>3,000+</td><td>5,000+</td><td>10,000+</td><td>25,000+</td><td>50,000+</td></tr>
    <tr><td>Price</td><td>$0.69</td><td>$1.14</td><td>$0.94</td><td>$0.89</td><td>$0.84</td><td>$0.74</td><td>$0.69</td></tr></table>
    <div class="btns"><div>REQUEST A QUOTE</div><div>BUY NOW</div><div>ORDER FREE SAMPLE</div></div>
    <div class="optlabel">IMPRINT OPTIONS</div>
    <div class="opts">
      <div class="opt"><h3>In-Stock Production</h3><p>Orders of 288 pcs or more</p><div class="inc">INCLUDES 1 IMPRINT COLOR</div>
        <dl><dt>Imprint Size</dt><dd>:</dd><dd>4" W x 7" H</dd><dt>Additional Colors 288 PCS</dt><dd>:</dd><dd>$0.74 each</dd><dt>Additional Colors 500+ pcs</dt><dd>:</dd><dd>$0.54 each</dd><dt>Full color Imprint 288 pcs</dt><dd>:</dd><dd>$0.99 each</dd><dt>Full color Imprint 500+ pcs</dt><dd>:</dd><dd>$0.79 each</dd><dt>Set Up Fee</dt><dd>:</dd><dd>$55 per color</dd><dt>Full Color Set Up Fee</dt><dd>:</dd><dd>$95 per color</dd></dl></div>
      <div class="opt"><h3>Overseas Production</h3><p>Orders of 1,000 pcs or more</p><div class="inc">FREE 1 COLOR, 2 LOCATION IMPRINT</div>
        <dl><dt>Imprint Size</dt><dd>:</dd><dd>Unlimited</dd><dt>Additional Colors 288 PCS</dt><dd>:</dd><dd>$0.74 each</dd><dt>Additional Colors 500+ pcs</dt><dd>:</dd><dd>$0.54 each</dd><dt>Full color Imprint 288 pcs</dt><dd>:</dd><dd>$0.99 each</dd><dt>Full color Imprint 500+ pcs</dt><dd>:</dd><dd>$0.79 each</dd><dt>Set Up Fee</dt><dd>:</dd><dd>$55 per color</dd><dt>Full Color Set Up Fee</dt><dd>:</dd><dd>$95 per color</dd></dl></div>
    </div>
  </div>
  <div class="abs sample">
    <h2>Complete this form &amp; receive a free sample</h2>
    <div class="fields"><div>Name</div><div>Email</div><div>Phone</div><div>Quantity<svg style="position:absolute;right:16px;top:15px" width="12" height="8" viewBox="0 0 12 8"><path d="M1 1l5 5 5-5" fill="none" stroke="#333" stroke-width="2"/></svg></div></div>
    <div class="submit">SUBMIT</div>
  </div>
  <h2 class="abs revhead"><span class="circ l"></span>Customer Reviews (38)<span class="circ r"></span></h2>
  <div class="abs rcard" style="left:8px"><h4>DANIEL R - <span>★★★★★</span></h4>Great product. I really am amazed and impressed with this company. They were very patient when assisting me find this item.</div>
  <div class="abs rcard" style="left:310px"><h4>OWEN L - <span>★★★★★</span></h4>After consulting with the staff, I ended up going with this bag instead of what I originally thought I wanted. They even sent me samples so I could compare. Thrilled with BHG.</div>
  <div class="abs rcard" style="left:611px"><h4>SAM K - <span>★★★★★</span></h4>I was looking specifically for a non-woven bag to use for my event and was delighted to find these. A+ customer service</div>
</section>

<div class="abs tabs"><div class="on" style="width:168px">DETAILS</div><div style="width:198px">REVIEWS</div><div style="width:264px">ADDITIONAL INFO</div><div style="width:282px;border:0">SHIPPING ESTIMATOR</div></div>
<section class="abs details">
  <h2>Non-Woven Promotional Tote Bags Wholesale</h2>
  <div class="row"><b>NAME</b><i>:</i>Non-Woven Reusable Promo Totes</div>
  <div class="row"><b>SKU</b><i>:</i>PP2</div>
  <div class="row"><b>SIZE</b><i>:</i>13" W x 14" H x 7" D</div>
  <div class="row"><b>THICKNESS</b><i>:</i>100 GSM</div>
  <div class="row"><b>AVAILABLE COLORS</b><i>:</i>Black, Hunter Green, Kelly Green, Lime Green, Maui Blue, Navy Blue, Purple, Red, Royal Blue, Tan, Teal &amp; Yellow</div>
  <div class="row"><b>IMPRINT AREA</b><i>:</i>8" W x 8" H</div>
  <div class="row"><b>KEY FEATURES</b><i>:</i>• Spacious Main Compartment, 1274 Cubic Inches</div>
  <ul class="feat"><li>22” Carry Straps</li><li>Made from 100 GSM Non-Woven Polypropylene</li><li>Eco-Friendly and 100% Recyclable</li><li>Removable Hard Bottom Insert at the Base</li><li>5 Day Standard Production / RUSH service available</li><li>10 Day Production for Full Color Artwork</li><li>8” Wide x 8” High Imprint Area</li><li>Made From Recycled Content</li></ul>
</section>

<section class="abs recs">
  <h2 class="abs revhead" style="top:26px"><span class="circ l"></span>Recommended Products<span class="circ r"></span></h2>
  <div class="rec" style="left:26px"><div class="pic" role="img" aria-label="Purple, green and red printed tote bags" style="background:linear-gradient(135deg,#6a3aa6,#2fc24a 50%,#d9302e)"></div>Size: 13" W x 14" H x 7" D<br>As Low As: $0.54<br>SKU: PP9<br><span class="st">★★★★★</span><small>38 Review(s)</small></div>
  <div class="rec" style="left:252px"><div class="pic" role="img" aria-label="Blue and red printed tote bags" style="background:linear-gradient(135deg,#1c6fb5 45%,#d9302e 55%)"></div>Size: 13" W x 14" H x 7" D<br>As Low As: $0.54<br>SKU: PP9<br><span class="st">★★★★★</span><small>38 Review(s)</small></div>
  <div class="rec" style="left:479px"><div class="pic" role="img" aria-label="Green and tan printed tote bags" style="background:linear-gradient(135deg,#23913f 48%,#c9b28b 52%)"></div>Size: 13" W x 14" H x 7" D<br>As Low As: $0.54<br>SKU: PP9<br><span class="st">★★★★★</span><small>38 Review(s)</small></div>
  <div class="rec" style="left:705px"><div class="pic" role="img" aria-label="Purple and tan printed tote bags" style="background:linear-gradient(135deg,#5b3aa6 45%,#d7b889 55%)"></div>Size: 13" W x 14" H x 7" D<br>As Low As: $0.54<br>SKU: PP9<br><span class="st">★★★★★</span><small>38 Review(s)</small></div>
</section>

<footer class="abs footer">
  <div class="fcol" style="left:145px;width:240px"><div class="fbrand"><i></i>Bright Harbor Goods</div>
    <p style="margin-top:22px;line-height:21px">Bright Harbor Goods is an eco-friendly company that specializes in manufacturing custom bags. BHG was founded in 2009 and has strived to make the world a better place ever since.</p>
    <div class="social"><b></b><b></b><b></b><b></b><b></b></div></div>
  <div class="fcol" style="left:441px"><h3>Useful Links</h3>Customer Service<br>Our Story<br>Site Map<br>FTC Disclosure<br>Privacy Policy<br>Contact Us<br>Art &amp; Imprint Policy<br>Free Rush</div>
  <div class="fcol" style="left:626px"><h3>Why Buy From Us</h3>Reusable Bag Stats<br>Best Price Guarantee<br>Return &amp; Refund Policy<br>Shipping Policy<br>In-Stock &amp; Custom Production<br>Frequently Asked Questions</div>
  <div class="fcol" style="left:857px"><h3>Address</h3>480 Harbor Lane, Suite 12<br>Bayview, FL 33000<br><br>Phone: 1-800-555-0142<br><br>Email: info@brightharborgoods.example</div>
</footer>
<div class="abs copy">Copyright &nbsp;© 2020 BrightHarborGoods.example. &nbsp;&nbsp;All rights reserved.</div>
<div class="abs chat"><div class="face" role="img" aria-label="Support agent portrait"></div>CHAT NOW!</div>
</body>
</html>
```